Post card for landscape service

Velmora Property Management**FEATURED SERVICE*** Weekly Lawn mowing service starting at $15/ cutting ****other services****landscape servicespring and fall clean uplawn and flowerbed care (pest and weed control)fertilizing plantingand moreCall for a Free estimate!!10% off first months service with signed contract

Please make double sided ( a front and a back)

Target Market(s)

home owners

Industry/Entity Type

Landscape

Requirements
Must have
• please feture the weekly lawn mowing service and then list the other sevices
• contact info... can be found on business card that was uploaded.
• must say residential services
Should not have
• please dont list reo management

```html
<!DOCTYPE html>
<html lang="en">
<head>
<meta charset="utf-8">
<title>Velmora Property Management – Postcard</title>
<link href="https://fonts.googleapis.com/css2?family=Carlito:wght@400;700&family=Encode+Sans+Condensed:wght@600&display=swap" rel="stylesheet">
<style>
  :root {
    --ink: #0a0a0a;
    --paper: #fafaf8;
    --leaf: #3cae1c;
    --leaf-dark: #2f8f12;
    --grass-light: #7fe02a;
    --grass-mid: #4cbf14;
    --grass-deep: #2f8f0c;
    --white: #ffffff;
  }
  html, body {
    margin: 0;
    padding: 0;
    overflow: hidden;
    background: var(--ink);
  }
  .postcard {
    position: relative;
    width: 1200px;
    height: 862px;
    background: var(--ink);
    overflow: hidden;
    font-family: "Carlito", "Calibri", sans-serif;
  }
  .grass-band {
    position: absolute;
    left: 292px;
    top: 254px;
    width: 908px;
    height: 362px;
    background:
      radial-gradient(ellipse at 70% 20%, var(--grass-light) 0%, transparent 55%),
      linear-gradient(180deg, var(--grass-light) 0%, var(--grass-mid) 45%, var(--grass-deep) 100%);
  }
  .side-panel {
    position: absolute;
    inset: 0;
    width: 320px;
    height: 862px;
  }
  .service-list {
    position: absolute;
    left: 0;
    top: 0;
    width: 250px;
    height: 862px;
    margin: 0;
    padding: 0;
    list-style: none;
    color: var(--leaf);
    font-weight: 700;
    font-size: 38px;
    line-height: 1;
    text-align: center;
  }
  .service-list li {
    position: absolute;
    left: 0;
    width: 250px;
    transform: translateY(-50%);
  }
  .service-list .ornament {
    left: 109px;
    width: 32px;
    height: 32px;
    border-radius: 50%;
    background: var(--leaf);
  }
  .brand-name {
    position: absolute;
    left: 288px;
    top: 74px;
    width: 860px;
    margin: 0;
    transform: translateY(-50%);
    font-family: "Encode Sans Condensed", "Arial Narrow", sans-serif;
    font-weight: 600;
    font-size: 71px;
    letter-spacing: -1px;
    color: var(--leaf);
    text-align: center;
    white-space: nowrap;
  }
  .brand-tagline {
    position: absolute;
    left: 288px;
    top: 158px;
    width: 860px;
    margin: 0;
    transform: translateY(-50%);
    font-weight: 400;
    font-size: 66px;
    color: var(--leaf);
    text-align: center;
    white-space: nowrap;
  }
  .contact-block {
    position: absolute;
    left: 376px;
    top: 0;
    color: var(--white);
    font-weight: 700;
    font-size: 42px;
    text-shadow: 0 1px 3px rgba(0,0,0,0.35);
  }
  .contact-block p {
    position: absolute;
    left: 0;
    margin: 0;
    white-space: nowrap;
    transform: translateY(-50%);
  }
  .contact-block .label-small { font-size: 36px; }
  .contact-block .number {
    font-family: "Encode Sans Condensed", "Arial Narrow", sans-serif;
    font-size: 44px;
    letter-spacing: -1.5px;
  }
  .feature {
    position: absolute;
    left: 300px;
    width: 856px;
    margin: 0;
    transform: translateY(-50%);
    color: var(--leaf);
    font-weight: 400;
    font-size: 62px;
    text-align: center;
    white-space: nowrap;
  }
</style>
</head>
<body>
<main class="postcard">
  <div class="grass-band" role="img" aria-label="Photo of a lush green mown lawn"></div>

  <svg class="side-panel" viewBox="0 0 320 862" aria-hidden="true">
    <path d="M0,0 L185,0 C270,120 305,300 300,440 C296,600 260,740 195,862 L0,862 Z" fill="var(--paper)"/>
    <path d="M185,0 C270,120 305,300 300,440 C296,600 260,740 195,862" fill="none" stroke="var(--leaf)" stroke-width="7"/>
  </svg>

  <ul class="service-list">
    <li style="top:88px">Spring</li>
    <li style="top:143px">&amp;</li>
    <li style="top:198px">Fall</li>
    <li style="top:254px">cleanup</li>
    <li class="ornament" style="top:306px" role="img" aria-label="Heart and vine ornament"></li>
    <li style="top:365px">Lawn</li>
    <li style="top:419px">&amp;</li>
    <li style="top:474px">Flowerbeds</li>
    <li class="ornament" style="top:528px" role="img" aria-label="Heart and vine ornament"></li>
    <li style="top:586px">Planting,</li>
    <li style="top:641px; left:14px">pest control,</li>
    <li style="top:696px">fertilizing</li>
    <li style="top:752px">&amp; more</li>
  </ul>

  <h1 class="brand-name">Velmora Property Management</h1>
  <p class="brand-tagline">commercial and residential</p>

  <div class="contact-block">
    <p style="top:318px"><span class="label-small">Office</span> <span class="number">908-555-0142</span></p>
    <p style="top:379px">Cell&nbsp;&nbsp;&nbsp;<span class="number">906-555-0187</span></p>
    <p style="top:442px">Call for a free estimate</p>
    <p style="top:506px">10% off 1st months service</p>
    <p style="top:569px">with contract</p>
  </div>

  <p class="feature" style="top:700px">Weekly Lawn Mowing Service</p>
  <p class="feature" style="top:784px">Starting at $15</p>
</main>
</body>
</html>
```